Small, static, 2 page website that promotes 3-6 workshops

This is a microsite for my company that promotes 3 (and later 6) security workshops for developers. The address is going to be codewacht-cursussen.nl so it is very important that the title reads 'Codewacht Cursussen' and the subtitle reads 'voor ontwikkelaars' (means for developers in dutch).

On the frontpage, there will be a small introduction text (about 50 words) about the workshops in general and there should be 3 workshops listed on the frontpage with also a small introduction text. All the workshops are cyber security/hacking related so maybe a small graphic for every workshop would lighten things up.

Then when a visitor clicks a 'more info' button a detail page about that specific workshop with a longer description, a date/location, a 'book now' button and a price should be show.

I have include a quick drawing of what I have in mind for the frontpage, this is not set in stone so you could come up with something else.

I also included my company logo, it should be clear on the site that these workshops are 'Halvard Shield' workshops.

Target Market(s)

Development companies looking for security workshops, the responsible people for those type of workshops are usually security officers, lead developers/managers or developers themselves.

Industry/Entity Type

It Company

Number of Pages Required

2 page

Font styles to use
Sans Serif
Other font styles liked:

Requirements
Must have
• 3 highlighted trainings on the frontpage and a detail page and the title and subtitle as headings on the page.
Nice to have
• I'd really like to have the 3 boxes on the frontpage to have icons or some sort of images. The first 3 workshops that are going to be on the page are:
• - Security awareness for developers
• - Web application security from a hackers perspective
• - Penetrationtesting for developers

```html
<!DOCTYPE html>
<html lang="nl">
<head>
<meta charset="utf-8">
<title>Codewacht Cursussen – Halvard Shield</title>
<link href="https://fonts.googleapis.com/css2?family=Orbitron:wght@500;600;700&family=Montserrat:wght@400;500;600;700&display=swap" rel="stylesheet">
<style>
:root{
  --navy:#1b3a6b;
  --grey-head:#6e6e6e;
  --text:#222;
  --muted:#707070;
  --white:#fff;
  --dark:#0b1218;
  --footer:#0d0d0d;
  --band:rgba(22,22,22,.78);
  --testi:#3d5f93;
}
*{margin:0;padding:0;box-sizing:border-box}
html,body{width:730px;height:1200px;overflow:hidden;background:var(--white)}
body{font-family:"Montserrat",sans-serif;color:var(--text);position:relative}
.head-font{font-family:"Orbitron","Montserrat",sans-serif;font-weight:700}

.site-header{position:absolute;top:0;left:0;width:730px;height:58px;background:var(--white);border-bottom:1px solid #ddd}
.brand{position:absolute;left:48px;top:11px;display:flex;align-items:center;gap:10px}
.brand-mark{width:34px;height:34px;background:var(--navy)}
.brand-name{font-family:"Orbitron",sans-serif;font-weight:600;font-size:15px;line-height:17px;color:var(--navy);letter-spacing:1.5px}
.contact{position:absolute;top:16px;display:flex;gap:8px;align-items:center;font-size:8px;line-height:12px}
.contact .label{color:var(--navy);font-weight:600}
.contact .value{color:var(--text);font-weight:600}
.contact svg{width:26px;height:26px}
.call{left:392px}.mail{left:498px}
.menu-btn{position:absolute;left:659px;top:16px;width:22px;height:22px;border:2px solid var(--navy);border-radius:4px}

.hero{position:absolute;top:58px;left:0;width:730px;height:323px;
  background:
    radial-gradient(ellipse 60% 50% at 50% 20%,rgba(255,255,255,.55),transparent 70%),
    linear-gradient(180deg,#e6edf2 0%,#c9d2d8 30%,#9a8f86 60%,#5b4a40 100%)}
.hero-arrow{position:absolute;top:138px;width:17px;height:20px;background:#222;display:flex;align-items:center;justify-content:center}
.hero-arrow.prev{left:32px}.hero-arrow.next{right:31px}
.hero-caption{position:absolute;left:0;bottom:0;width:730px;height:45px;background:var(--band);color:var(--white);font-size:20px;font-weight:600;text-align:center;line-height:45px;letter-spacing:-.3px}

.section-title{font-size:17px;text-align:center;letter-spacing:.3px}
.divider{position:relative;width:390px;height:12px;margin:0 auto}
.divider::before{content:"";position:absolute;left:0;right:0;top:6px;height:1px;background:currentColor;opacity:.35}
.divider span{position:absolute;left:189px;top:1px;width:11px;height:11px;border-radius:50%;background:currentColor}

.about{position:absolute;top:381px;left:0;width:730px;height:207px;text-align:center}
.about .section-title{margin-top:34px;color:var(--grey-head)}
.about .section-title b{color:var(--navy);font-weight:700}
.about .divider{margin-top:8px;color:#7a8aa5}
.about .lead{font-size:10px;font-weight:600;margin-top:13px}
.about .body{font-size:8.4px;line-height:15.6px;color:var(--muted);margin:9px auto 0;width:680px}

.workshops{position:absolute;top:588px;left:0;width:730px;height:364px;background:radial-gradient(circle at 60% 45%,#1f3b52 0%,#0f1d2a 45%,var(--dark) 100%);color:var(--white);text-align:center}
.workshops .section-title{margin-top:38px}
.workshops .divider{margin-top:8px;width:230px;color:#c8d2dc}
.workshops .divider span{left:109px}
.workshops .intro{font-size:9.6px;font-weight:600;line-height:17.5px;margin:12px auto 0;width:660px}
.workshop{position:absolute;top:152px;width:200px;text-align:center}
.workshop .icon{width:70px;height:64px;margin:0 auto;background:var(--white);border-radius:10px 10px 35px 35px;display:flex;align-items:center;justify-content:center}
.workshop .icon svg{width:30px;height:30px}
.workshop h3{font-family:"Orbitron",sans-serif;font-weight:600;font-size:8.6px;line-height:13px;margin-top:16px;letter-spacing:.3px}
.workshop p{font-size:7.6px;line-height:12.2px;margin-top:4px;color:#e4e8ec}
.read-more{display:inline-flex;align-items:center;gap:4px;margin-top:12px}
.read-more .mark{width:15px;height:15px;background:var(--white)}
.read-more span{background:var(--white);color:var(--text);font-size:7.8px;font-weight:600;padding:3px 6px}

.testimonials{position:absolute;top:952px;left:0;width:730px;height:208px;background:linear-gradient(180deg,#47699c 0%,var(--testi) 60%,#2e4a77 100%);color:var(--white)}
.testimonials .section-title{margin-top:30px}
.testimonials .divider{margin-top:6px;width:260px;color:#c9d4e5}
.testimonials .divider span{left:124px}
.avatar{position:absolute;left:52px;top:86px;width:84px;height:84px;border-radius:50%;background:#e7ebf0;border:3px solid #fff}
.quote{position:absolute;left:167px;top:84px;width:512px;font-size:7.9px;font-weight:600;line-height:15.4px}
.quote::before{content:"\201C";color:#9fb0c8;font-size:15px;margin-right:6px;vertical-align:-4px}
.quote-rule{position:absolute;left:167px;top:152px;width:512px;height:1px;background:rgba(255,255,255,.3)}
.author{position:absolute;left:169px;top:165px;font-family:"Orbitron",sans-serif;font-weight:600;font-size:7.8px}
.dots{position:absolute;left:655px;top:167px;display:flex;gap:3px}
.dots i{width:6px;height:6px;border-radius:50%;background:#fff}
.dots i:first-child{background:none;border:1px solid #fff}

.site-footer{position:absolute;top:1160px;left:0;width:730px;height:40px;background:var(--footer);color:var(--white)}
.copyright{position:absolute;left:49px;top:15px;font-family:"Orbitron",sans-serif;font-weight:600;font-size:7.4px}
.social{position:absolute;top:9px;left:572px;display:flex;gap:7px}
.social i{width:22px;height:22px;border-radius:50%;background:var(--white)}
</style>
</head>
<body>

<header class="site-header">
  <div class="brand">
    <div class="brand-mark"></div>
    <div class="brand-name">HALVARD<br>SHIELD</div>
  </div>
  <div class="contact call">
    <svg viewBox="0 0 26 26" aria-hidden="true"><path d="M3 4h20v9c0 6-5 9-10 11C8 22 3 19 3 13z" fill="none" stroke="#1b3a6b" stroke-width="1.6"/><path d="M10 9c-1 3 1 7 5 8l1.5-1.5-2-1.5-1 .8c-1.2-.6-2-1.6-2.3-2.8l.8-1-1.4-2z" fill="#1b3a6b"/></svg>
    <div><div class="label">Call Us:</div><div class="value">020-555-0147</div></div>
  </div>
  <div class="contact mail">
    <svg viewBox="0 0 26 26" aria-hidden="true"><path d="M3 4h20v9c0 6-5 9-10 11C8 22 3 19 3 13z" fill="none" stroke="#1b3a6b" stroke-width="1.6"/><rect x="8" y="9" width="10" height="7" fill="none" stroke="#1b3a6b" stroke-width="1.3"/><path d="M8 9l5 4 5-4" fill="none" stroke="#1b3a6b" stroke-width="1.3"/></svg>
    <div><div class="label">Mail Us:</div><div class="value">info@halvardshield.nl</div></div>
  </div>
  <div class="menu-btn">
    <svg viewBox="0 0 18 18" width="18" height="18" aria-hidden="true"><g fill="#1b3a6b"><rect x="3" y="4" width="2" height="2"/><rect x="6" y="4" width="9" height="2"/><rect x="3" y="8" width="2" height="2"/><rect x="6" y="8" width="9" height="2"/><rect x="3" y="12" width="2" height="2"/><rect x="6" y="12" width="9" height="2"/></g></svg>
  </div>
</header>

<section class="hero" role="img" aria-label="Photo of a trainer presenting to a seated audience in a bright classroom">
  <div class="hero-arrow prev"><svg width="8" height="10" viewBox="0 0 8 10"><path d="M6 1L2 5l4 4" stroke="#fff" fill="none" stroke-width="1.2"/></svg></div>
  <div class="hero-arrow next"><svg width="8" height="10" viewBox="0 0 8 10"><path d="M2 1l4 4-4 4" stroke="#fff" fill="none" stroke-width="1.2"/></svg></div>
  <h1 class="hero-caption">CODEWACHT CURSUSSEN, VOOR ONTWIKKELAARS</h1>
</section>

<section class="about">
  <h2 class="section-title head-font">ABOUT <b>CODEWACHT CURSUSSEN</b></h2>
  <div class="divider"><span></span></div>
  <p class="lead">Lorem ipsum dolor sit amet, consectetuer adipiscing elit, sed diam nonummy nibh euismod tincidunt ut laoreet dolore</p>
  <p class="body">Ut wisi enim adi minim veniam, quis nostrudk exerci tation more ullamcorper suscipit lobortis nis ut aliquip commodo conseqti. Duis autem iriure dolor in hendrerit in vulputate veesseml molestie consequat, vel illum facilisi. Lorem ipsum dolor sit amet, conse ctetuer adipiscing elit, sedmoi di nonummy nibh &nbsp;commodo consequat. Duis autem vel eum iriurel dolor in hendrerit. Ut wisi enim adi minim veniam, quis nostrudk exerci tation more ullamcorper suscipit lobortis nis ut aliquip commodo conseqti. Duis autemiriure dolor in hendrerit in vulputate veesseml molestie</p>
</section>

<section class="workshops" aria-label="Our workshops">
  <h2 class="section-title head-font">OUR WORKSHOPS</h2>
  <div class="divider"><span></span></div>
  <p class="intro">Ut wisi enim adi minim veniam, quis nostrudk exerci tation more ullamcorper suscipit lobortis nis ut aliquip commodo conseqti. Duis autem iriure dolor in hendrerit in vulputate veesseml molestie consequat, vel illum facilisi. Lorem ipsum dolor</p>

  <article class="workshop" style="left:50px">
    <div class="icon"><svg viewBox="0 0 30 30" aria-hidden="true"><path d="M7 15l6 6 11-12" fill="none" stroke="#0f1d2a" stroke-width="3.2" stroke-linecap="round" stroke-linejoin="round"/></svg></div>
    <h3>Security Awareness For<br>Developers</h3>
    <p>Lorem ipsum dolor sit amet, consectetuer adipiscing elit, sed diam nonummy nibh euismod tincidunt ut laoreet dolore magna aliquam</p>
    <div class="read-more"><i class="mark"></i><span>Read More</span></div>
  </article>
  <article class="workshop" style="left:265px">
    <div class="icon"><svg viewBox="0 0 30 30" aria-hidden="true"><rect x="6" y="7" width="18" height="12" rx="1" fill="#0f1d2a"/><rect x="3" y="20" width="24" height="3" rx="1" fill="#0f1d2a"/></svg></div>
    <h3>Web application security from a<br>hackers perspective</h3>
    <p>Lorem ipsum dolor sit amet, consectetuer adipiscing elit, sed diam nonummy nibh euismod tincidunt ut laoreet dolore magna aliquam</p>
    <div class="read-more"><i class="mark"></i><span>Read More</span></div>
  </article>
  <article class="workshop" style="left:480px">
    <div class="icon"><svg viewBox="0 0 30 30" aria-hidden="true"><circle cx="15" cy="15" r="9" fill="none" stroke="#0f1d2a" stroke-width="2.4"/><circle cx="15" cy="15" r="3" fill="#0f1d2a"/><path d="M15 2v6M15 22v6M2 15h6M22 15h6" stroke="#0f1d2a" stroke-width="2.4"/></svg></div>
    <h3>Penetrationtesting For<br>Developers</h3>
    <p>Lorem ipsum dolor sit amet, consectetuer adipiscing elit, sed diam nonummy nibh euismod tincidunt ut laoreet dolore magna aliquam</p>
    <div class="read-more"><i class="mark"></i><span>Read More</span></div>
  </article>
</section>

<section class="testimonials" aria-label="Client testimonials">
  <h2 class="section-title head-font">CLIENT TESTIMONIALS</h2>
  <div class="divider"><span></span></div>
  <div class="avatar" role="img" aria-label="Portrait photo of the client"></div>
  <p class="quote">Lorem ipsum dolor smit amet, consectetuer adipiscing elitmk, sed amet diam nonummy nibh euismodl tincidun nt utmi laoreetmlhoi dolore magna aliquam erat volutpat. Ut wisi enim ad minim veniam, quis nostrud exer tationk ullamcori permona suscipit lobortisk nisl utml mot aliqpi ex ea commodo consequat. Duis autem vel eumk iriurek dolor inj hendrerit inn vulputate velit esse molestiemo consequat, velhkinl illumn gnol dolore eu feugiat nullamo facilisis.</p>
  <div class="quote-rule"></div>
  <div class="author">- Mr. Joren Dekkers</div>
  <div class="dots"><i></i><i></i><i></i></div>
</section>

<footer class="site-footer">
  <p class="copyright">Copyright © 2017 CODEWACHT CURSUSSEN. All Rights Reserved</p>
  <div class="social" aria-label="Social media links"><i></i><i></i><i></i><i></i></div>
</footer>

</body>
</html>
```